Event Website for the Audio & Visual Industry

Convene is an exhibition aimed at meeting the business needs of audio and visual professionals – the visitors are the ones that make purchase decisions when buying anything to do with AV installation, Lighting & Entertainment Technology, DJ Technologies and even Musical Instruments.

We need to rebuild our website to reflect the professional look but with a bit of creativity/flare that is associated with the industry.

Websites whose design is along the lines we're looking for:

• http:www.marlowtech.com.au
• http:www.quenra.com
• http://www.brightpanelfair.example/ (competitor expo, like the layout. Not fantastic though, but the best I’ve seen from the industry)
• http://www.velmora.com.au and http://www.tralvick.com.au/ (Like these brand websites, they are clean and corporate but the use of imagery allows it to have some personality)

Target Market(s)

Corporate AV End Users, Lighting Designers, Concert/Entertainment companies, Sound Engineers

Industry/Entity Type

Business

Requirements
Must have
• Refer to the current splash page – www.convene-expo.example
This is the look and feel we have developed for our brochure. We want to expand on this and create a professional corporate look and feel without alienating existing sound, light and vision sectors.

The website's focus is to register visitors to attend the show. Please include a floating 'Register Free' Call to action. Please also include floating social media buttons. For what I mean by 'floating' check out the Social media buttons on this website: http://feedlorn.example/2012/02/19/glass-tower-trailer/ (scroll down to see effect).

We'll like to include a Rotating Banner at the top.

Sponsor element at the bottom off the page.

Sign up form functionality

Menu to be: About the Show, What's On, Register, How to Exhibit, Blog, Contact us.

I would like to see designs for a content page as well as the homepage.

```html
<!DOCTYPE html>
<html lang="en">
<head>
<meta charset="utf-8">
<title>Convene 2012</title>
<link href="https://fonts.googleapis.com/css2?family=Roboto+Condensed:wght@400;700&family=EB+Garamond:ital@0;1&family=Arimo&display=swap" rel="stylesheet">
<style>
  :root {
    --page-bg: #ececec;
    --ink: #111111;
    --nav-grey: #6b6b6b;
    --accent-red: #e3101b;
    --ribbon-red: #c8040e;
    --ribbon-dark: #8e0208;
    --rule: #d6d6d6;
    --caption-bg: rgba(0,0,0,0.82);
    --caption-text: #a9a9a9;
    --arrow: #4a4a4a;
  }
  * { margin: 0; padding: 0; box-sizing: border-box; }
  html, body { width: 960px; height: 1200px; overflow: hidden; }
  body {
    background: var(--page-bg);
    font-family: "Roboto Condensed", sans-serif;
    position: relative;
  }
  .header-glow {
    position: absolute; left: 0; top: -120px; width: 520px; height: 320px;
    background: radial-gradient(ellipse at center, #ffffff 30%, rgba(255,255,255,0) 70%);
  }
  .header-glow--right {
    left: 420px; width: 540px;
    background: radial-gradient(ellipse at center, #ffffff 25%, rgba(255,255,255,0) 70%);
  }
  .site-header { position: absolute; left: 96px; top: 0; width: 768px; height: 156px; border-bottom: 1px solid var(--rule); }
  .brand { position: absolute; left: 0; top: 36px; display: flex; align-items: center; gap: 12px; }
  .brand-mark { width: 14px; height: 14px; border-radius: 50%; background: var(--accent-red); }
  .brand-name { font-family: "Roboto Condensed", sans-serif; font-weight: 700; font-size: 58px; line-height: 1; color: var(--ink); }
  .event-info { position: absolute; right: 90px; top: 38px; text-align: right; }
  .event-dates { font-size: 20px; font-weight: 700; color: var(--ink); line-height: 24px; letter-spacing: -0.2px; }
  .event-venue { font-size: 13px; color: var(--accent-red); line-height: 16px; }
  .event-place { font-family: "EB Garamond", serif; font-style: italic; font-size: 11.5px; color: #555; line-height: 16px; }
  .register-ribbon { position: absolute; right: 0; top: 0; width: 74px; height: 126px; }
  .register-ribbon-text { position: absolute; left: 0; width: 74px; text-align: center; color: #fff; }
  .register-ribbon-text--small { top: 58px; font-size: 9.5px; }
  .register-ribbon-text--big { top: 68px; font-size: 15px; font-weight: 700; }
  .main-nav { position: absolute; right: 2px; top: 137px; display: flex; gap: 21px; list-style: none; }
  .main-nav li { font-size: 12px; color: var(--nav-grey); text-transform: uppercase; }
  .hero-slider {
    position: absolute; left: 96px; top: 182px; width: 768px; height: 297px;
    border-radius: 3px;
    background: linear-gradient(90deg, #e6e6e6 0%, #ffffff 5%, #ffffff 95%, #e6e6e6 100%);
  }
  .hero-shadow {
    position: absolute; left: 120px; top: 476px; width: 720px; height: 14px;
    border-radius: 50%;
    background: radial-gradient(ellipse at center top, rgba(0,0,0,0.55) 0%, rgba(0,0,0,0) 70%);
  }
  .hero-image {
    position: absolute; left: 43px; top: 0; width: 682px; height: 297px;
    background: linear-gradient(180deg, #6e4a34 0%, #8fb4cc 22%, #7a5440 45%, #3a2c2a 70%, #1e1a1d 100%);
  }
  .hero-caption {
    position: absolute; left: 0; bottom: 0; width: 100%; height: 81px;
    background: var(--caption-bg); padding: 11px 15px 0;
  }
  .hero-caption-title { font-size: 17.5px; color: #fff; line-height: 22px; }
  .hero-caption-text { font-family: "Arimo", sans-serif; font-size: 10.4px; line-height: 14px; color: var(--caption-text); margin-top: 5px; }
  .slider-arrow { position: absolute; top: 136px; width: 16px; height: 24px; }
  .slider-arrow--prev { left: 14px; }
  .slider-arrow--next { right: 14px; }
</style>
</head>
<body>
  <div class="header-glow"></div>
  <div class="header-glow header-glow--right"></div>

  <header class="site-header">
    <div class="brand">
      <span class="brand-mark"></span>
      <span class="brand-name">Convene</span>
    </div>

    <div class="event-info">
      <div class="event-dates">21ST - 23RD AUGUST 2012</div>
      <div class="event-venue">HARBOURSIDE CONVENTION &amp; EXHIBITION CENTRE</div>
      <div class="event-place">Wharf Quarter, Australia</div>
    </div>

    <a class="register-ribbon" href="#register">
      <svg width="74" height="126" viewBox="0 0 74 126">
        <defs>
          <linearGradient id="ribbonFill" x1="0" y1="0" x2="1" y2="0">
            <stop offset="0" stop-color="#d3050f"/>
            <stop offset="0.5" stop-color="#b8030b"/>
            <stop offset="1" stop-color="#d3050f"/>
          </linearGradient>
        </defs>
        <path d="M0 0 H74 V126 L37 96 L0 126 Z" fill="url(#ribbonFill)"/>
        <path d="M0 0 H2 V124 L0 126 Z M72 0 H74 V126 L72 124 Z" fill="#8e0208"/>
        <g transform="translate(37 33) rotate(45)" fill="#ffffff">
          <rect x="-4" y="-17" width="8" height="5" rx="1"/>
          <rect x="-4" y="-11" width="8" height="18"/>
          <path d="M-4 8 H4 L0 16 Z"/>
        </g>
      </svg>
      <span class="register-ribbon-text register-ribbon-text--small">REGISTER</span>
      <span class="register-ribbon-text register-ribbon-text--big">FREE</span>
    </a>

    <ul class="main-nav">
      <li>About the Show</li>
      <li>What's On</li>
      <li>Register</li>
      <li>How to Exhibit</li>
      <li>Blog</li>
      <li>Contact Us</li>
    </ul>
  </header>

  <div class="hero-shadow"></div>
  <section class="hero-slider">
    <svg class="slider-arrow slider-arrow--prev" viewBox="0 0 16 24"><path d="M13 2 L4 12 L13 22" fill="none" stroke="#4a4a4a" stroke-width="4"/></svg>
    <div class="hero-image" role="img" aria-label="Photo of a concert hall with sound engineers at mixing desks facing a brightly lit stage">
      <div class="hero-caption">
        <div class="hero-caption-title">Convene 2011 - The Best of the best last year...</div>
        <p class="hero-caption-text">Nullam pretium auctor massa ut consequat. Etiam hendrerit iaculis mattis. Proin tincidunt gravida augue in tempor. Proin blandit, elit a consectetur tincidunt, velit quam tristique risus, eget ultrices lorem dui ut nisl pretium auctor massa ut cons.</p>
      </div>
    </div>
    <svg class="slider-arrow slider-arrow--next" viewBox="0 0 16 24"><path d="M3 2 L12 12 L3 22" fill="none" stroke="#7a7a7a" stroke-width="4"/></svg>
  </section>
</body>
</html>
```